Zielgruppe
Ich suche ein ansprechendes Cover-Design für mein E-Book. Es handelt sich um einen Ratgeber über Selbstliebe und meine Zielgruppe sind Frauen im Alter zwischen 18 und 40 Jahren.
Aufgabenstellung
Klare Designs, die das Thema des Ratgebers unterstreichen und nicht durch unnötige Details und unlesbare Verschnörkelungen ablenken. Die weibliche Zielgruppe sollte vor allem angesprochen werden, dies sollte auch in der Farbauswahl berücksichtigt werden. Das bedeutet helle Farbtöne wie rosa, rot, hellblau oder pastellgelb.
Die Umsetzung des Motivs überlasse ich der Kreativität des Designers. Es können sowohl Stockfotos von einer jungen Frau gewählt werden, die Freude ausstrahlt und sich wohl in ihrer Haut fühlt (wo vielleicht auch warmes Licht oder Sonnenschein auf dem Cover zu sehen sind) oder ein rein graphisches Bild aus zusammengesetzten Elementen, die eine junge Frau zeigen und ihre Beziehung zur Selbstliebe deutlich wird. Es muss nicht zwangsläufig ein Herz abgebildet werden, nur weil es das erste ist, was man vielleicht mit Liebe assoziiert, auch wenn ein kreativer Umgang mit dem Herz als Symbol eine durchaus ansprechende Wirkung haben kann. Wichtig wäre mir eine kreative Umsetzung im Bild, wodurch das Thema der 'Selbstliebe' sofort deutlich wird und den Käufer anspricht. Der Titel sollte genauso deutlich hervorstechen wie das zentrale Motiv. Außerdem sollte gleich erkennbar sein, dass es sich nicht um einen Roman, sondern um einen Ratgeber handelt. Daher bin ich an einer graphischen Aufbereitung genauso wie an einem Fotomotiv interessiert. Bereits existierende Cover zu einem ähnlichen Ratgeber- Thema, die ich ansprechend finde, füge ich im Anhang hinzu.
Bitte nicht die im Anhang eingefügten Dateien verwenden, da sie urheberrechtlich geschützt sind! Sie dienen nur als Interpretationsvorschlag.
Titel: Gelassen atmen
Untertitel: Wie du Gewohnheiten änderst und mehr Klarheit im täglichen Alltag gewinnst
Autorenname: Jora Wendt
Der Buchrücken soll farblich an das Cover angepasst werden. Der Buchrückentext folgt noch im Anhang.
Das E-Book wird es auch als Paperback Buch geben. Der Umfang des Ra..

```html
<!DOCTYPE html>
<html lang="de">
<head>
<meta charset="utf-8">
<title>Gelassen atmen – Jora Wendt</title>
<link rel="stylesheet" href="https://fonts.googleapis.com/css2?family=Permanent+Marker&family=Roboto:wght@400;500;700&display=block">
<style>
  :root {
    --backdrop: #e9e9ea;
    --sun-white: #fbf7ec;
    --sun-cream: #f7e6b0;
    --glow-yellow: #f2c232;
    --glow-orange: #e8891c;
    --ember: #c4461a;
    --earth-red: #8a2410;
    --deep-brown: #4a140c;
    --figure-dark: #5a1a10;
    --author-red: #7a1e12;
    --title-white: #fbfaf7;
    --subtitle-white: #ffffff;
  }
  * { box-sizing: border-box; margin: 0; padding: 0; }
  html, body {
    width: 1200px;
    height: 1200px;
    overflow: hidden;
    background: var(--backdrop);
  }
  .canvas {
    width: 1200px;
    height: 1200px;
    display: flex;
    align-items: center;
    justify-content: center;
  }
  .book-cover {
    position: relative;
    width: 734px;
    height: 1100px;
    overflow: hidden;
    box-shadow: 0 10px 30px rgba(0,0,0,0.18);
  }
  .cover-photo {
    position: absolute;
    inset: 0;
    background:
      radial-gradient(ellipse 60% 40% at 18% 40%, var(--sun-white) 0%, var(--sun-cream) 30%, rgba(242,194,50,0) 70%),
      linear-gradient(180deg, #f6dc8a 0%, var(--glow-yellow) 34%, var(--glow-orange) 52%, var(--ember) 68%, var(--earth-red) 84%, var(--deep-brown) 100%);
  }
  .motif-photo {
    position: absolute;
    top: 90px;
    left: 300px;
    width: 330px;
    height: 900px;
    border-radius: 46% 46% 30% 30% / 20% 20% 12% 12%;
    background: linear-gradient(180deg, rgba(150,60,20,0.55) 0%, rgba(120,40,18,0.8) 35%, rgba(90,26,16,0.9) 60%, rgba(90,26,16,0.5) 100%);
    filter: blur(6px);
  }
  .author-name {
    position: absolute;
    top: 175px;
    left: 250px;
    font-family: "Roboto", sans-serif;
    font-weight: 700;
    font-size: 30px;
    color: var(--author-red);
    letter-spacing: 0.3px;
  }
  .book-title {
    position: absolute;
    top: 600px;
    left: 30px;
    right: 20px;
    font-family: "Permanent Marker", "Comic Sans MS", cursive;
    font-weight: 400;
    font-size: 104px;
    line-height: 1.0;
    text-transform: uppercase;
    color: var(--title-white);
    text-shadow: 0 2px 6px rgba(60,15,5,0.35);
  }
  .book-title span { display: block; }
  .title-line-one { text-align: right; }
  .title-line-two { text-align: center; padding-left: 40px; }
  .book-subtitle {
    position: absolute;
    top: 900px;
    left: 30px;
    right: 30px;
    text-align: center;
    font-family: "Roboto", sans-serif;
    font-weight: 500;
    font-size: 28px;
    line-height: 1.3;
    color: var(--subtitle-white);
    text-shadow: 0 1px 4px rgba(40,10,5,0.4);
  }
</style>
</head>
<body>
  <main class="canvas">
    <article class="book-cover">
      <div class="cover-photo" role="img" aria-label="Foto: Wiese und Hügel im warmen Gegenlicht der Abendsonne"></div>
      <div class="motif-photo" role="img" aria-label="Foto: junge Frau im gestreiften Shirt und Rock, als Silhouette im Gegenlicht, die Arme freudig ausgebreitet"></div>
      <p class="author-name">Jora Wendt</p>
      <h1 class="book-title"><span class="title-line-one">Gelassen</span><span class="title-line-two">atmen</span></h1>
      <p class="book-subtitle">Wie du Gewohnheiten änderst<br>und mehr Klarheit im täglichen Alltag gewinnst</p>
    </article>
  </main>
</body>
</html>
```